Flyer Design for a Boston Therapeutic Clinic

I am a body therapist who needs a couple of flyers designed:
1. To fit half a page.
2. To fit a 5 inch by 3.5 inch flyer.
My practice is based in Boston, MA and my web site is:
www.LarchTessvik.Com
For the First half page:
A. Have my company's name and color shown as it appears on my web site (Larch Tessvik)
B. Have the following text: "Control your weight (This part should be emphasized) by balancing your nervous and digestive system through the Tessvik Method. The Tessvik Method, a technique developed by Dr. Mara. Tessvik, uses physical pressure to manipulate visceral tissue to bring back resiliency and proper functioning of the whole body."
Also helps with
-Constipation
-Bloating
-IBS
-eating disorders and overeating
Our practitioner is highly experienced. Please visit our web sites for reviews.
C. I would like to have a nice earthy feeling, something that feels "freeing" like open flowers, or an open land scape such as mountains or fields.
D. I also like the color blue, white, orange; perhaps if these colors can be integrated into the flyer, that would be great.
E. "Visit our web site LarchTessvik.com or call 786-555-0148"
The Smaller Flyer :
A.The smaller Flyer should also have my Company's name as shown on my web site (Larch Tessvik)
B.The following text: " Restore your body's natural resiliency and greatly reduce your physical pain through the Dr. Mara Tessvik Method of Structural Integration."
C. "Our practitioner is highly experienced and has a great reputation; visit our web site for reviews."
"Benefits:
"reduce aches and pains
reduce joint pain
reduce chronic muscular tension"
D, "feel better after the first session!"
E. if you could use a picture of me working on someone from my web site, that would be great.
F. I also like the colors white, orange and silver, for this one.
G. "Visit our web site LarchTessvik.com or call 786-555 0148"
I am very open minded,
I would like the flyer to evoke a sense of tranquility, professionalism, and simplicity. So if you have another angle you think would look good, then go for it! As long as it looks clean, professional and helpful.
Thanks a lot!
If you need any pictures from my web site, I have the original high resolution files that i can send.
Professionals and working men and women from ages 20-70
Clinic

```html
<!DOCTYPE html>
<html lang="en">
<head>
<meta charset="utf-8">
<title>Larch Tessvik Therapy — Flyer</title>
<link rel="stylesheet" href="https://fonts.googleapis.com/css2?family=Cutive&family=Arvo:wght@700&display=swap">
<style>
  :root {
    --cream: #f6f8d6;
    --cream-light: #fbfce8;
    --leaf-dark: #2f5a1c;
    --leaf: #5b9a2c;
    --leaf-light: #b6d67a;
    --badge-blue: #2c4594;
    --badge-blue-deep: #1f3478;
    --brand-red: #e0452a;
    --ink-gray: #58625c;
    --label-blue: #2438c8;
    --photo-warm: #b8402a;
    --photo-dark: #5a1e14;
    --white: #ffffff;
  }
  html, body {
    margin: 0;
    padding: 0;
    width: 1200px;
    height: 857px;
    overflow: hidden;
    background: var(--white);
  }
  .flyer {
    position: relative;
    width: 1200px;
    height: 857px;
    overflow: hidden;
    background: linear-gradient(90deg, var(--cream) 0%, var(--cream-light) 60%, var(--cream) 100%);
    font-family: "Cutive", "Courier New", serif;
  }
  .hero-photo {
    position: absolute;
    left: 0;
    top: 0;
    width: 660px;
    height: 857px;
    background:
      radial-gradient(ellipse at 30% 20%, rgba(230,245,200,0.8) 0%, rgba(230,245,200,0) 40%),
      linear-gradient(180deg, var(--leaf-light) 0%, var(--leaf) 45%, var(--leaf-dark) 100%);
    -webkit-mask-image: linear-gradient(90deg, #000 0%, #000 62%, transparent 100%);
    mask-image: linear-gradient(90deg, #000 0%, #000 62%, transparent 100%);
  }
  .badge {
    position: absolute;
    left: 60px;
    top: 40px;
    width: 252px;
    height: 252px;
    border-radius: 50%;
    background: radial-gradient(circle at 40% 35%, var(--badge-blue) 0%, var(--badge-blue-deep) 100%);
  }
  .badge-text {
    position: absolute;
    left: 0;
    top: 0;
    width: 252px;
    height: 252px;
    display: flex;
    align-items: center;
    justify-content: center;
    text-align: center;
    color: var(--white);
    font-family: "Arvo", Georgia, serif;
    font-weight: 700;
    font-size: 30px;
    line-height: 38px;
    transform: rotate(-17deg);
  }
  .brand-title {
    position: absolute;
    left: 416px;
    top: 38px;
    margin: 0;
    font-weight: 400;
    font-size: 54px;
    line-height: 70px;
    white-space: nowrap;
    letter-spacing: 1px;
  }
  .brand-name { color: var(--brand-red); }
  .brand-service { color: var(--ink-gray); }
  .intro {
    position: absolute;
    left: 458px;
    top: 112px;
    margin: 0;
    color: var(--ink-gray);
    font-size: 35px;
    line-height: 53px;
    letter-spacing: 1.4px;
    white-space: nowrap;
  }
  .benefits {
    position: absolute;
    left: 460px;
    top: 394px;
    margin: 0;
    color: var(--brand-red);
    font-size: 26px;
    line-height: 37px;
    letter-spacing: 0.8px;
    white-space: nowrap;
  }
  .benefits-label { color: var(--label-blue); }
  .reputation {
    position: absolute;
    left: 458px;
    top: 490px;
    margin: 0;
    color: var(--ink-gray);
    font-size: 24.5px;
    line-height: 35px;
    letter-spacing: 1px;
    white-space: nowrap;
  }
  .session-photo {
    position: absolute;
    left: 347px;
    top: 618px;
    width: 254px;
    height: 184px;
    border: 7px solid var(--white);
    background: linear-gradient(135deg, var(--photo-warm) 0%, #c9573a 45%, var(--photo-dark) 100%);
  }
  .contact {
    position: absolute;
    left: 610px;
    top: 630px;
    width: 560px;
    margin: 0;
    text-align: center;
    color: var(--brand-red);
    font-size: 37px;
    line-height: 60px;
    white-space: nowrap;
  }
</style>
</head>
<body>
  <main class="flyer">
    <div class="hero-photo" role="img" aria-label="Woman raising her arms in a lush green tropical forest, seen from behind"></div>

    <div class="badge">
      <div class="badge-text">Feel<br>Better<br>After the<br>First<br>Session</div>
    </div>

    <h1 class="brand-title"><span class="brand-name">Larch Tessvik</span> <span class="brand-service">Therapy</span></h1>

    <p class="intro">Restore your body's natural<br>resiliency and greatly reduce<br>your physical pain through the<br>Dr. Mara Tessvik Method of<br>Structural Integration.</p>

    <p class="benefits"><span class="benefits-label">Benefits:</span> Reduce aches and pains, Reduce<br>joint pain reduce chronic muscular tension</p>

    <p class="reputation">Our practitioner is highly experienced and<br>has a great reputation; visit our web site for<br>reviews.</p>

    <div class="session-photo" role="img" aria-label="Practitioner's hands working on a client's body during a session"></div>

    <p class="contact">Visit our website<br>www.LarchTessvik.com<br>or call 786-555-0148</p>
  </main>
</body>
</html>
```